Family business needs stationery redesign with new logo

Family owned company, established in 1987 wanting a brand 'refresh'. We are an electrical, refrigeration and construction company based in the Barkly Region Northern Territory, Australia. We have a new logo we would like to use which is uploaded along with our current letterhead and email signature. We are also dropping the word 'contractors' so please do not include this on any designs. Please note also, the 'orange' color used in our logo and designs should be Northern Territory red ochre which is as follows:

RGB (Hex): #C75B12
PantoneĀ® 159 C
CMYK: 1 / 74 / 100 / 7

We are needing our stationery redesigned using our new logo. Please include letterheads, business cards, envelopes, and email signatures.

We currently use our business letterheads for quotations, invoices, letters, HR matters, and internal memos.

We also need a separate simplified letterhead for internal paperwork such as employee leave forms, meeting agendas, and meeting minutes etc.
Updates

Reason: Needing more submissions of full package designs. We are wanting all our stationery, including business cards, letterheads, email signatures, envelopes, etc to be cohesive. We also require ALL the information, as supplied on our template letterhead, to be included on the new letterhead designs. including electrical license no.etc Thank you, R&K

Reason: needing more time as work has got in the way of looking over designs. A lot of designs not meeting the brief/criteria.

Industry/Entity Type

Business

Colors
0355a3
f37122

Requirements
Must have
• The 'orange' color used in the designs should be Northern Territory red ochre which is as follows:
• RGB (Hex): #C75B12
• PantoneĀ® 159 C
• CMYK: 1 / 74 / 100 / 7
• ***MUST INCLUDE ALL INFORMATION THAT IS ON OUR CURRENT LETTERHEAD***
Should not have
• Please do not include the word 'contractors'

```html
<!DOCTYPE html>
<html lang="en">
<head>
<meta charset="utf-8">
<title>R&amp;K Business Card</title>
<link rel="stylesheet" href="https://fonts.googleapis.com/css2?family=Arimo:ital,wght@0,400;0,700;1,400&display=swap">
<style>
  :root {
    --page-bg: #d8d4cf;
    --card-bg: #eef0f1;
    --navy: #1f2b5c;
    --ochre: #c75b12;
    --ink: #1a1a1a;
    --divider: #8a8f99;
    --web-text: #c9cedb;
  }
  * { margin: 0; padding: 0; box-sizing: border-box; }
  html, body {
    width: 1200px; height: 969px; overflow: hidden;
    background: var(--page-bg);
    font-family: "Arimo", Arial, sans-serif;
  }
  .business-card {
    position: absolute; left: 100px; top: 200px;
    width: 1000px; height: 566px;
    background: var(--card-bg);
    border-radius: 26px;
    overflow: hidden;
    box-shadow: 0 6px 24px rgba(0,0,0,0.12);
  }
  .brand-name {
    position: absolute; left: 267px; top: 271px;
    transform: translate(-50%, -50%);
    font-weight: 700; font-size: 108px; letter-spacing: 2px;
    color: var(--navy);
  }
  .divider {
    position: absolute; left: 514px; top: 129px;
    width: 2px; height: 276px; background: var(--divider); opacity: 0.6;
  }
  .contact-block { position: absolute; left: 566px; top: 128px; }
  .person-name {
    font-weight: 700; font-size: 35px; color: var(--navy); line-height: 1.1;
    letter-spacing: 0.5px;
  }
  .person-title { font-size: 27px; color: var(--ochre); line-height: 1.25; }
  .address { margin-top: 28px; font-size: 25px; color: var(--ink); line-height: 1.4; }
  .contact-list { list-style: none; margin-top: 18px; }
  .contact-list li {
    display: flex; align-items: center; gap: 14px;
    font-size: 25px; color: var(--ink); line-height: 38px;
  }
  .contact-list svg { width: 24px; height: 24px; fill: var(--navy); flex: none; }
  .bottom-band { position: absolute; left: 0; bottom: 0; width: 1000px; height: 100px; }
  .website {
    position: absolute; left: 478px; top: 540px;
    transform: translate(-50%, -50%);
    font-style: italic; font-size: 24px; letter-spacing: 3px; color: var(--web-text);
  }
</style>
</head>
<body>
  <div class="business-card">
    <div class="brand-name">R&amp;K</div>
    <div class="divider"></div>

    <div class="contact-block">
      <p class="person-name">DANIEL HART</p>
      <p class="person-title">CEO/Founder</p>
      <p class="address">3921 Wattle Grove Lane<br>Tennant Creek, NT 0860</p>
      <ul class="contact-list">
        <li>
          <svg viewBox="0 0 24 24" aria-hidden="true"><path d="M6.6 10.8a15.1 15.1 0 0 0 6.6 6.6l2.2-2.2a1 1 0 0 1 1-.25 11.4 11.4 0 0 0 3.6.57 1 1 0 0 1 1 1V20a1 1 0 0 1-1 1A17 17 0 0 1 3 4a1 1 0 0 1 1-1h3.5a1 1 0 0 1 1 1c0 1.25.2 2.45.57 3.57a1 1 0 0 1-.25 1z"/></svg>
          614 208 3379
        </li>
        <li>
          <svg viewBox="0 0 24 24" aria-hidden="true"><path d="M6 3h12v5H6zM4 9h16a2 2 0 0 1 2 2v6h-4v4H6v-4H2v-6a2 2 0 0 1 2-2zm4 7v3h8v-3z"/></svg>
          614 208 3380
        </li>
        <li>
          <svg viewBox="0 0 24 24" aria-hidden="true"><path d="M2 5h20v14H2zm2 2v.5l8 5 8-5V7l-8 5z"/></svg>
          hello@rkgroup.com
        </li>
      </ul>
    </div>

    <svg class="bottom-band" viewBox="0 466 1000 100" preserveAspectRatio="none" aria-hidden="true">
      <path d="M60 532 Q475 470 1000 552 L1000 566 L0 566 L0 540 Z" fill="var(--navy)"/>
      <path d="M60 526 Q475 462 1000 546" fill="none" stroke="var(--ochre)" stroke-width="4"/>
    </svg>
    <div class="website">www.rkgroup.com</div>
  </div>
</body>
</html>
```